hobby beef jerky maker looking to break into the commercial market

We need product labels designed for each flavour of jerky we make. Currently have 3 flavours that we are ready to share with the world. We need in your face designs to help us stand out from an already crowded market.
The product name is Rowdy Beef Jerky.
The flavours we offer have been named Porch Party, Tangy Glow and Fiery Bite.
The Rowdy Beef Jerky Title should remain the same across the three labels but the design for each flavour can change as you see fit.
Label needs to fit within 110mm x 110mm to suit our current packaging

Industry/Entity Type

Food Production

Logo Text

Morvathen Clover

Colors

Designer to choose colors to be used in the design.

Requirements
Must have
• "Rowdy Beef Jerky" font and colour must remain the same across the 3 designs
Nice to have
• The labels will be used on the clear side of the packaging with a small space towards the bottom being left visible so the product inside can be seen

```html
<!DOCTYPE html>
<html lang="en">
<head>
<meta charset="utf-8">
<title>Rowdy Beef Jerky – Tangy Glow Label</title>
<link rel="stylesheet" href="https://fonts.googleapis.com/css2?family=Lobster&display=swap">
<style>
  :root {
    --cream: #eeddb8;
    --pattern-tone: #e3d0a6;
    --slate: #5e6758;
    --crimson: #a01c3a;
    --ink: #1f2419;
  }
  html, body {
    margin: 0;
    padding: 0;
    width: 1200px;
    height: 1200px;
    overflow: hidden;
    background: var(--cream);
  }
  .label {
    display: block;
    width: 1200px;
    height: 1200px;
  }
  .script {
    font-family: "Lobster", cursive;
  }
  .brand-line {
    fill: var(--slate);
    font-size: 128px;
  }
  .brand-arc {
    fill: var(--slate);
    font-size: 122px;
  }
  .flavour {
    fill: var(--cream);
    stroke: var(--slate);
    stroke-width: 14px;
    stroke-linejoin: round;
    paint-order: stroke fill;
    font-size: 150px;
  }
  .frame {
    fill: none;
    stroke: var(--slate);
    stroke-width: 6;
  }
  .rule-dark { stroke: var(--ink); stroke-width: 2.5; }
  .rule-red { stroke: var(--crimson); stroke-width: 3; }
  .zig-dark { fill: none; stroke: var(--ink); stroke-width: 5; }
  .zig-red { fill: none; stroke: var(--crimson); stroke-width: 5; }
</style>
</head>
<body>
<svg class="label" viewBox="0 0 1200 1200" xmlns="http://www.w3.org/2000/svg">
  <defs>
    <radialGradient id="backdrop-tone" cx="50%" cy="50%" r="60%">
      <stop offset="0%" stop-color="var(--pattern-tone)"/>
      <stop offset="100%" stop-color="var(--cream)"/>
    </radialGradient>
    <path id="brand-curve" d="M 120 480 Q 600 170 1090 480"/>
  </defs>

  <rect class="backdrop" role="img" aria-label="Soft floral mandala pattern in pale tan behind the label" x="0" y="0" width="1200" height="1200" fill="url(#backdrop-tone)"/>

  <rect class="frame" x="30" y="28" width="1142" height="1144" rx="37" ry="37"/>

  <g class="title-rules">
    <line class="rule-dark" x1="128" y1="140" x2="366" y2="140"/>
    <line class="rule-red" x1="92" y1="159" x2="366" y2="159"/>
    <line class="rule-dark" x1="128" y1="177" x2="366" y2="177"/>
    <line class="rule-dark" x1="830" y1="140" x2="1068" y2="140"/>
    <line class="rule-red" x1="830" y1="159" x2="1104" y2="159"/>
    <line class="rule-dark" x1="830" y1="177" x2="1068" y2="177"/>
  </g>

  <text class="script brand-line" x="600" y="205" text-anchor="middle">Rowdy</text>
  <text class="script brand-arc" text-anchor="middle">
    <textPath href="#brand-curve" startOffset="50%">Beef Jerky</textPath>
  </text>

  <path class="flames" role="img" aria-label="Bold crimson flames rising across the lower half of the label"
        fill="var(--crimson)"
        d="M 55 1044 L 55 760 Q 55 640 180 640 L 380 640 Q 420 440 600 356 Q 780 440 820 640 L 1020 640 Q 1137 640 1137 760 L 1137 1044 Z"/>

  <g class="flavour-name" transform="rotate(-22 600 900)">
    <text class="script flavour" x="560" y="880" text-anchor="middle">Tangy</text>
    <text class="script flavour" x="700" y="1000" text-anchor="middle">Glow</text>
  </g>

  <g class="zigzags">
    <polyline class="zig-dark" points="63,1062 107,1054 151,1070 195,1054 239,1070 283,1054 327,1070 371,1054 415,1070 459,1054 503,1070 547,1054 591,1070 635,1054 679,1070 723,1054 767,1070 811,1054 855,1070 899,1054 943,1070 987,1054 1031,1070 1075,1054 1137,1062"/>
    <polyline class="zig-red" points="63,1080 107,1072 151,1088 195,1072 239,1088 283,1072 327,1088 371,1072 415,1088 459,1072 503,1088 547,1072 591,1088 635,1072 679,1088 723,1072 767,1088 811,1072 855,1088 899,1072 943,1088 987,1072 1031,1088 1075,1072 1137,1080"/>
    <polyline class="zig-dark" points="63,1098 107,1090 151,1106 195,1090 239,1106 283,1090 327,1106 371,1090 415,1106 459,1090 503,1106 547,1090 591,1106 635,1090 679,1106 723,1090 767,1106 811,1090 855,1106 899,1090 943,1106 987,1090 1031,1106 1075,1090 1137,1098"/>
  </g>
</svg>
</body>
</html>
```